Business Card Logo for an Accountant (a Steady Ledger)

I would like a logo to put on my business card for an accountant. I am seasoned, skilled and give TLC to my clients. I have over 40 years of experience and love to teach people how to do accounting for their businesses. I am an accountant who can envision a fix to any problem.

Business Card will have this on it:

Loretta Quimbeck
dba Steady Ledger
Cell (555) 417-3082

```html
<!DOCTYPE html>
<html lang="en">
<head>
<meta charset="utf-8">
<title>Steady Ledger – Business Card</title>
<link href="https://fonts.googleapis.com/css2?family=Open+Sans:wght@400;700&display=swap" rel="stylesheet">
<style>
  :root {
    --page-bg: #2e2e2f;
    --card-white: #ffffff;
    --brand-red: #7a0a0e;
    --swoosh-grey: #8e8e8e;
    --text-grey: #5a5a5a;
    --logo-ring: #6b6b6b;
  }
  * { box-sizing: border-box; margin: 0; padding: 0; }
  html, body {
    width: 1200px; height: 900px; overflow: hidden;
    background: var(--page-bg);
    font-family: "Open Sans", Arial, sans-serif;
  }
  .card {
    position: absolute;
    left: 270px;
    width: 660px; height: 378px;
    background: var(--card-white);
    border-radius: 26px;
    overflow: hidden;
    box-shadow: 0 10px 30px rgba(0,0,0,.45);
  }
  .card--front { top: 50px; }
  .card--back { top: 472px; }
  .card-shapes { position: absolute; inset: 0; }

  .brand {
    position: absolute;
    display: flex; align-items: center; gap: 18px;
    white-space: nowrap;
  }
  .brand-dot {
    flex: none;
    width: 86px; height: 86px; border-radius: 50%;
    border: 6px solid var(--logo-ring);
  }
  .brand-name {
    color: var(--brand-red);
    font-weight: 700;
    font-size: 34px;
    line-height: 1;
    letter-spacing: .5px;
  }
  .card--front .brand { left: 42px; top: 70px; }
  .card--back .brand { left: 50%; top: 50%; transform: translate(-50%, -50%); }
  .card--back .brand-name { font-size: 40px; }

  .person {
    position: absolute; left: 46px; top: 250px;
  }
  .person-name {
    color: var(--brand-red); font-weight: 700; font-size: 21px;
  }
  .person-role {
    color: var(--text-grey); font-size: 19px; margin-top: 2px;
  }

  .contact {
    position: absolute; right: 28px; top: 212px;
    color: var(--card-white); font-size: 16px; text-align: right;
    line-height: 1.7; white-space: nowrap;
  }
  .contact-line { display: flex; justify-content: flex-end; align-items: center; gap: 8px; }
  .contact-icon { width: 15px; height: 15px; fill: var(--card-white); }
</style>
</head>
<body>

<section class="card card--front">
  <svg class="card-shapes" viewBox="0 0 660 378" width="660" height="378" aria-hidden="true">
    <path d="M465 0 H660 V378 H170 C360 340 470 240 465 0 Z" fill="var(--brand-red)"/>
    <path d="M120 368 C320 336 455 250 440 60 C435 250 300 320 120 346 Z" fill="var(--swoosh-grey)"/>
  </svg>

  <div class="brand">
    <div class="brand-dot"></div>
    <span class="brand-name">Steady Ledger</span>
  </div>

  <div class="person">
    <div class="person-name">Loretta Quimbeck</div>
    <div class="person-role">Principal</div>
  </div>

  <div class="contact">
    <div class="contact-line">(555) 417-3082
      <svg class="contact-icon" viewBox="0 0 24 24"><path d="M6.6 10.8a15.1 15.1 0 0 0 6.6 6.6l2.2-2.2a1 1 0 0 1 1-.25 11.4 11.4 0 0 0 3.6.57 1 1 0 0 1 1 1V20a1 1 0 0 1-1 1A17 17 0 0 1 3 4a1 1 0 0 1 1-1h3.5a1 1 0 0 1 1 1c0 1.25.2 2.450.57 3.6a1 1 0 0 1-.25 1z"/></svg>
    </div>
    <div class="contact-line">steadyledger@mailbox.net
      <svg class="contact-icon" viewBox="0 0 24 24"><path d="M2 5h20v14H2z M4 7v.5l8 5 8-5V7l-8 5z" fill-rule="evenodd"/></svg>
    </div>
  </div>
</section>

<section class="card card--back">
  <div class="brand">
    <div class="brand-dot"></div>
    <span class="brand-name">Steady Ledger</span>
  </div>
</section>

</body>
</html>
```